Business Card Design for Massage Therapist

*I am a qualified massage therapist & require a business card for my new business 'Tidal Touch & Wellness'.
*Contact details I'd like included on the card are: Elise Brantry, Mobile: 0481562930, Email: tidaltw@mailvane.com
*It is a massage business dedicated to providing quality therapeutic massage treatments, that will later incorporate natural therapies.
* Styles Include: Swedish, Relaxation, Pregnancy, Deep Tissue & Sports Massage
*I offer the styles of massage as listed above & a mobile service that allows clients to book a massage in the comfort of their own home.
*I'd like my logo to be fairly simple, streamlined, modern & reflect what my business services are - one people will easily remember.
*I'd like the colors to represent & emit a sense of calm, be fresh, welcoming, natural colors that appeal to a wide range of people.
*Colors I'd like to see are: pale blue, aqua & greens.

Target Market(s)

Both Male & Female, aged 20 to 65, singles, couples, parents, business people who are interested in their health, fitness & general wellbeing and maintenance. Located in the Harbourvale area and surrounding suburbs of Melbourne.

Industry/Entity Type

Massage

Requirements
Must have
• Fonts used in logos should be owned by the designer.
Should not have
• I don't want the design to have someone being massaged in it (pictures/photos) or have it look too clinical & sterile.

```html
<!DOCTYPE html>
<html lang="en">
<head>
<meta charset="utf-8">
<title>Tidal Touch &amp; Wellness — Business Card</title>
<link rel="stylesheet" href="https://fonts.googleapis.com/css2?family=Didact+Gothic&display=swap">
<style>
  :root {
    --backdrop: #9a9a9a;
    --card-white: #ffffff;
    --brand-blue: #3f74bb;
    --brand-teal: #37b49c;
    --band-teal: #2fb39a;
    --panel-top: #5b92d0;
    --panel-bottom: #3c6fb3;
    --mint: #8ee6bd;
    --text-white: #ffffff;
    --shadow: rgba(0, 0, 0, 0.28);
  }
  * { box-sizing: border-box; margin: 0; padding: 0; }
  html, body {
    width: 1200px;
    height: 900px;
    overflow: hidden;
    background: var(--backdrop);
    font-family: "Didact Gothic", sans-serif;
  }
  .canvas {
    position: relative;
    width: 1200px;
    height: 900px;
  }
  .business-card {
    position: absolute;
    left: 100px;
    top: 145px;
    width: 1000px;
    height: 611px;
    background: var(--card-white);
    box-shadow: 0 10px 30px var(--shadow);
    overflow: hidden;
  }
  .card-panel {
    position: absolute;
    inset: 0;
    width: 1000px;
    height: 611px;
  }
  .brand {
    position: absolute;
    left: 70px;
    top: 108px;
    display: flex;
    align-items: center;
    gap: 26px;
  }
  .brand-dot {
    width: 74px;
    height: 74px;
    border-radius: 50%;
    background: var(--brand-teal);
  }
  .brand-name {
    font-size: 50px;
    color: var(--brand-blue);
    font-weight: 400;
    letter-spacing: 0.5px;
  }
  .contact {
    position: absolute;
    left: 70px;
    top: 288px;
  }
  .contact-name {
    font-size: 33px;
    color: var(--mint);
    line-height: 1.1;
  }
  .contact-role {
    font-size: 25px;
    color: var(--text-white);
    margin-top: 6px;
  }
  .contact-lines {
    position: absolute;
    left: 70px;
    top: 432px;
    font-size: 28px;
    line-height: 40px;
  }
  .contact-label { color: var(--mint); display: inline-block; width: 108px; }
  .contact-value { color: var(--text-white); }
  .divider {
    position: absolute;
    left: 528px;
    top: 280px;
    width: 2px;
    height: 218px;
    background: var(--text-white);
  }
  .services {
    position: absolute;
    left: 572px;
    top: 266px;
    list-style: none;
    font-size: 25px;
    line-height: 34px;
    color: var(--text-white);
  }
  .services-title {
    color: var(--mint);
  }
</style>
</head>
<body>
<main class="canvas">
  <section class="business-card" aria-label="Tidal Touch &amp; Wellness business card">
    <svg class="card-panel" viewBox="0 0 1000 611" aria-hidden="true">
      <defs>
        <linearGradient id="panelGradient" x1="0" y1="0" x2="0" y2="1">
          <stop offset="0" stop-color="var(--panel-top)"/>
          <stop offset="1" stop-color="var(--panel-bottom)"/>
        </linearGradient>
      </defs>
      <polygon points="0,256 1000,236 1000,611 0,611" fill="url(#panelGradient)"/>
      <polygon points="0,246 1000,226 1000,238 0,258" fill="var(--band-teal)"/>
    </svg>

    <div class="brand">
      <span class="brand-dot"></span>
      <span class="brand-name">Tidal Touch &amp; Wellness</span>
    </div>

    <div class="contact">
      <p class="contact-name">Elise Brantry</p>
      <p class="contact-role">Massage Therapist</p>
    </div>

    <div class="contact-lines">
      <p><span class="contact-label">Mobile:</span><span class="contact-value">0481562930</span></p>
      <p><span class="contact-label">Email&nbsp;:</span><span class="contact-value">tidaltw@mailvane.com</span></p>
    </div>

    <span class="divider"></span>

    <ul class="services">
      <li class="services-title">Massage Services:</li>
      <li>Swedish/Relaxation</li>
      <li>Pregnancy</li>
      <li>Deep Tissue</li>
      <li>Sports</li>
      <li>Corporate</li>
    </ul>
  </section>
</main>
</body>
</html>
```